Cover design for series of 4 Best Practice Guides

The Design Brief
We are looking for cover designs for a series of 4 industry Best Practice Guides (BPG):

1. Best Practice Guide: Repossessions
2. Best Practice Guide: Collections
3. Best Practice Guide: Investigations
4. Best Practice Guide: Process Serving

The only essential elements to be included in the design are:
1. our logo (attached in both blue and white - either is acceptable)
2. Publication Name

We are looking for a set of 4 clean and professional looking designs which are clearly linked/related but where each BPG is distinguishable as a different publication either by the use of colour or by the use of appropriate imagery (illustrations, appropriate photos etc).

The BPGs will be produced in both A4 hard copy and electronic format.

Files should be provided in either AI or PSD format.

Some Background Information
These BPGs are being produced by the Guild of Ledgerwick Brokers ([login to view URL]) an industry association in Australia representing collectors, investigators, process servers and repossession agents. Broadly known as mercantile agents, below is a brief description of each role:

o Collectors make demands for payment of overdue debts (often pursuant to a formal contract) and enter into dialogue with individual and corporate debtors in order to achieve resolution of delinquent accounts whether by full or part recovery or by establishing the debtor does not have the means to pay.

o Investigators inquire into, and obtain information about, the personal character or actions of persons, together with the character or nature of the business or occupation of any person.

o Process servers deliver court issued process for a variety of reasons including debt recovery, family law proceedings, civil and criminal litigation in strict accordance with the rules of the issuing court.

o Repossession agents act for principals to formal contracts (leases, bills of sale, hire purchase agreements etc.) to either seek payment of arrears or the balance of the loan facility or else to recover the security for the facility (cars, motor cycles etc.).

Below is an extract from the Repossession BPG:

INTRODUCTION: BEST PRACTICE GUIDE
The Guild of Ledgerwick Brokers is the industry association nationally representing businesses and persons engaged in collections, investigations, process serving and repossession services in Australia.
Membership of the GLB is voluntary - businesses and persons join to demonstrate their commitment to the high standards adopted and promoted by the association.

This Best Practice Guide sets out best practice standards expected from members involved in the provision of repossession services and which debtors and businesses engaging with members should expect. Members agree to comply with this Best Practice Guide by virtue of membership.

We believe that this Best Practice Guide will enable debtors and businesses to address their situation involving the repossession of goods in confidence of fair treatment by members. To fulfil the potential of this Best Practice Guide those with debts outstanding for which repossession of goods is involved must cooperate with the businesses managing their debts including the repossession of security items so as to agree to reasonable solutions.

This Best Practice Guide is intended as a helpful resource for debtors and creditors, whilst compliance by members is intended to ensure best practice standards are maintained.

```html
<!DOCTYPE html>
<html lang="en">
<head>
<meta charset="utf-8">
<title>Best Practice Guides – Cover Series</title>
<link rel="stylesheet" href="https://fonts.googleapis.com/css2?family=Open+Sans:wght@700&display=swap">
<style>
  :root {
    --ink-navy: #2f2e66;
    --ink-black: #111111;
    --band-orange: #f26b22;
    --band-green: #3dae4a;
    --band-red: #d3232b;
    --band-navy: #2e2d62;
    --panel-yellow: #fde9a1;
    --panel-green: #d6e9cd;
    --panel-pink: #f3ddd1;
    --panel-lavender: #d9d5e9;
    --divider: #ffffff;
  }
  html, body {
    margin: 0;
    padding: 0;
    width: 849px;
    height: 1200px;
    overflow: hidden;
    background: var(--divider);
  }
  .series {
    position: relative;
    width: 849px;
    height: 1200px;
    display: grid;
    grid-template-columns: 423px 423px;
    grid-template-rows: 597px 600px;
    column-gap: 3px;
    row-gap: 3px;
    font-family: "Open Sans", Arial, sans-serif;
  }
  .cover {
    position: relative;
    overflow: hidden;
  }
  .cover__photo {
    position: absolute;
    left: 0; right: 0; top: 0;
    height: 298px;
  }
  .cover__band {
    position: absolute;
    left: 0; right: 0; top: 0;
    height: 68px;
    clip-path: polygon(0 0, 100% 0, 100% 100%, 0 42%);
  }
  .cover__panel {
    position: absolute;
    left: 0; right: 0; top: 298px; bottom: 0;
  }
  .cover__title {
    position: absolute;
    left: 30px;
    top: 20px;
    margin: 0;
    font-weight: 700;
    font-size: 42px;
    line-height: 62px;
    color: var(--ink-navy);
  }
  .cover__title .topic {
    display: block;
    color: var(--ink-black);
    font-size: 41px;
    margin-top: 8px;
    white-space: nowrap;
  }
  .brand {
    position: absolute;
    left: 230px;
    top: 40px;
    display: flex;
    align-items: center;
    gap: 10px;
    color: var(--ink-navy);
    font-weight: 700;
    font-size: 44px;
    letter-spacing: 4px;
  }
  .brand__dot {
    width: 14px; height: 14px;
    border-radius: 50%;
    background: var(--ink-navy);
  }

  .cover--repo .cover__band { background: var(--band-orange); }
  .cover--repo .cover__panel { background: var(--panel-yellow); }
  .cover--repo .cover__photo { background: linear-gradient(160deg, #f4f4f4 0%, #e7e2dc 45%, #8c6f5a 100%); }

  .cover--coll .cover__band { background: var(--band-green); }
  .cover--coll .cover__panel { background: var(--panel-green); }
  .cover--coll .cover__photo { background: linear-gradient(100deg, #4a3326 0%, #8a5a3c 45%, #a56f4a 100%); }

  .cover--inv .cover__band { background: var(--band-red); }
  .cover--inv .cover__panel { background: var(--panel-pink); }
  .cover--inv .cover__photo { background: linear-gradient(110deg, #3f5a2c 0%, #6e7a63 40%, #2a2a2a 75%, #9b9b9b 100%); }

  .cover--serve .cover__band { background: var(--band-navy); }
  .cover--serve .cover__panel { background: var(--panel-lavender); }
  .cover--serve .cover__photo { background: linear-gradient(120deg, #fafafa 0%, #e6d3a8 40%, #2b2b2b 70%, #1a1a1a 100%); }
</style>
</head>
<body>
<main class="series">
  <section class="cover cover--repo">
    <div class="cover__photo" role="img" aria-label="Photo of one hand passing car keys into another hand"></div>
    <div class="cover__band"></div>
    <div class="cover__panel">
      <h1 class="cover__title">Best<br>Practice<br>Guide:<span class="topic">Repossessions</span></h1>
      <div class="brand"><span class="brand__dot"></span>GLB</div>
    </div>
  </section>

  <section class="cover cover--coll">
    <div class="cover__photo" role="img" aria-label="Photo of a person knocking on a wooden door"></div>
    <div class="cover__band"></div>
    <div class="cover__panel">
      <h1 class="cover__title" style="top:6px">Best<br>Practice<br>Guide:<span class="topic">Collections</span></h1>
      <div class="brand" style="top:26px"><span class="brand__dot"></span>GLB</div>
    </div>
  </section>

  <section class="cover cover--inv">
    <div class="cover__photo" role="img" aria-label="Photo of an investigator photographing from a car window with a telephoto lens"></div>
    <div class="cover__band"></div>
    <div class="cover__panel">
      <h1 class="cover__title">Best<br>Practice<br>Guide:<span class="topic">Investigations</span></h1>
      <div class="brand"><span class="brand__dot"></span>GLB</div>
    </div>
  </section>

  <section class="cover cover--serve">
    <div class="cover__photo" role="img" aria-label="Photo of a person in a suit handing over an envelope"></div>
    <div class="cover__band"></div>
    <div class="cover__panel">
      <h1 class="cover__title" style="left:22px">Best<br>Practice<br>Guide:<span class="topic">Process Serving</span></h1>
      <div class="brand"><span class="brand__dot"></span>GLB</div>
    </div>
  </section>
</main>
</body>
</html>
```